VORTEK Studio Shape your ideas

VORTEK Studio is a soci% 26 # 233; t% 26 # 233; of mobile application design and multiexperience destiny% 26 # 233; % 26 # 224; The% 26 # 39; industry and particularly the watch industry% 26 # 232; re. By multiexperience, I mean applications usable on watches,% 26 # 233; holographic screens,% 26 # 233; touch screens g% 26 # 233; ant, r% 26 # 233; alit% 26 # 233; virtual,% 26 # 224; distance with a gripsense and% 26 # 233; obviously on mobile on tablet and smartphone. Applications will call% 26 # 224; 3d, artificial intelligence, big data. The company logo% 26 # 233; t% 26 # 233; is attached% 26 # 233; below.

Target Market(s)

Swiss precision industry Watchmaking industry% 26 # 232; re

Coding

Coded - Design and coding required

Font styles to use
Sans Serif

Colors

Designer to choose colors to be used in the design.

Requirements
Must have
• A Contact form A gallery of Vid% 26 # 233; o / Photo (portfolio) 3D images of% 26 # 39; illustration orient% 26 # 233; es industry but% 26 # 233; also luxury (take free images A partner page
Nice to have
• A blog
Should not have
• The designs are too loaded, the page should load quickly.

```html
<!DOCTYPE html>
<html lang="en">
<head>
<meta charset="utf-8">
<title>VORTEK Studio – The Ultimate Smart Watch</title>
<link href="https://fonts.googleapis.com/css2?family=Raleway:wght@300;400;500;600;700;800&display=swap" rel="stylesheet">
<style>
:root{
  --blue:#0a6fc2;
  --blue-dark:#0b4f93;
  --blue-bright:#1e88e5;
  --ink:#2b2f36;
  --text:#555a61;
  --muted:#8b9097;
  --line:#d9dde2;
  --gray-bg:#f2f3f5;
  --dark-bg:#262a31;
  --white:#ffffff;
}
*{margin:0;padding:0;box-sizing:border-box}
html,body{width:1200px;height:4065px;overflow:hidden}
body{font-family:"Raleway",sans-serif;color:var(--ink);background:var(--white);position:relative}
.abs{position:absolute}
section,header,footer{position:absolute;left:0;width:1200px}
a{text-decoration:none;color:inherit}

/* nav */
.site-nav{top:0;height:60px;background:var(--blue)}
.brand{left:95px;top:19px;color:var(--white);font-weight:700;font-size:18px;letter-spacing:1px;display:flex;align-items:center;gap:8px}
.brand-mark{width:14px;height:14px;background:var(--white)}
.nav-link{top:21px;color:var(--white);font-size:11px;font-weight:500;letter-spacing:.3px}
.nav-link.active{border-bottom:2px solid var(--white);padding-bottom:4px}

/* hero */
.hero{top:60px;height:540px;background:linear-gradient(180deg,#e4eef7 0%,#eef4fa 90%,#ffffff 100%)}
.hero-title{left:95px;top:130px;font-size:62px;font-weight:800;color:var(--blue-bright);letter-spacing:6px;line-height:1}
.hero-sub{left:95px;top:190px;font-size:35px;font-weight:500;line-height:47px;width:380px}
.hero-copy{left:95px;top:290px;width:370px;font-size:12.5px;line-height:22px;color:var(--text)}
.btn-outline{left:95px;top:376px;width:135px;height:31px;border:1.5px solid var(--ink);border-radius:16px;font-size:11px;font-weight:700;text-align:center;line-height:28px}
.hero-visual{left:505px;top:20px;width:650px;height:490px;border-radius:24px;background:linear-gradient(135deg,#cfe3f3 0%,#7fb4dc 35%,#22313f 60%,#4b8fc4 85%,#d8e9f6 100%)}

/* shared */
.section-title{font-size:36px;font-weight:500;letter-spacing:.5px;line-height:1.2}
.section-sub{font-size:14px;color:var(--text);line-height:21px}
.center{text-align:center;width:1200px;left:0}

/* features */
.features{top:600px;height:589px}
.feature{width:280px;text-align:center}
.watch-art{width:142px;height:233px;margin:0 auto;border-radius:18px;background:linear-gradient(180deg,#dfe3e7 0%,#2a3138 35%,#0b5d98 50%,#2a3138 65%,#dfe3e7 100%)}
.feature h3{font-size:20px;font-weight:600;margin-top:38px}
.feature p{font-size:12px;color:var(--muted);line-height:18px;margin-top:10px;padding:0 20px}

/* app section */
.app{top:1189px;height:494px;background:var(--gray-bg)}
.app-visual{left:95px;top:58px;width:537px;height:379px;border-radius:8px;background:linear-gradient(90deg,#5a2f9e 0%,#9b35d8 45%,#d94f8f 70%,#f47a45 100%)}
.check-list{left:682px;top:186px;width:460px}
.check-item{display:flex;gap:16px;margin-bottom:24px}
.ring{flex:none;width:32px;height:32px;border-radius:50%;border:3px solid #44c2d8;display:flex;align-items:center;justify-content:center}
.ring span{width:12px;height:12px;border-radius:3px;background:var(--blue)}
.check-item h4{font-size:21px;font-weight:500}
.check-item p{font-size:12px;color:var(--muted);line-height:18px;margin-top:6px;width:300px}

/* tech section */
.tech{top:1683px;height:493px;background:linear-gradient(90deg,#23272d 0%,#2d3239 45%,#4a5058 100%)}
.tech-visual{left:560px;top:0;width:640px;height:493px;background:linear-gradient(135deg,#3a4048 0%,#1b4f8c 45%,#102f55 70%,#4a5058 100%)}
.tech h2{color:var(--white)}
.tech .section-sub{color:#d4d7db}
.tech-list{left:95px;top:180px}
.tech-item{display:flex;align-items:center;gap:14px;height:56px;color:var(--white);font-size:17px;font-weight:500}
.tech-item .ring{border-color:#4a90e2;width:36px;height:36px}
.tech-item .ring span{background:#8fb8ea;border-radius:50%}

/* partners */
.partners{top:2176px;height:306px}
.partners p{left:95px;top:180px;width:430px;font-size:12px;line-height:22px;color:var(--text)}
.badge-grid{left:600px;top:98px;display:grid;grid-template-columns:repeat(4,124px);gap:4px}
.badge{height:50px;border:1px solid var(--line);display:flex;align-items:center;justify-content:center}
.badge span{width:64px;height:18px;border-radius:9px;background:#c9d3de}

/* health section */
.health{top:2482px;height:444px;background:linear-gradient(90deg,#b8ccd8 0%,#dbe6eb 55%,#eef3f4 100%)}
.health-visual{left:0;top:0;width:660px;height:444px;background:linear-gradient(120deg,#9fb9ca 0%,#c9a48f 40%,#e2685a 55%,#c7d6de 100%)}
.health p{left:682px;top:218px;width:440px;font-size:12px;line-height:22px;color:var(--text)}
.btn-solid{left:682px;top:302px;width:126px;height:30px;border-radius:15px;background:var(--blue-bright);color:var(--white);font-size:11px;font-weight:700;text-align:center;line-height:30px}

/* gallery + subscribe */
.subscribe{top:2926px;height:722px;background:linear-gradient(180deg,#ffffff 0,#ffffff 382px,#0b5ea8 382px,#0a4f92 100%)}
.gallery{left:166px;top:100px;width:868px;height:345px;display:flex;justify-content:space-between;align-items:flex-end}
.gallery-item{border-radius:28px}
.gallery-item.side{width:278px;height:300px}
.gallery-item.dark{background:linear-gradient(160deg,#1f6fc0 0%,#123a66 40%,#2a2e33 75%,#56595e 100%)}
.gallery-item.silver{background:linear-gradient(200deg,#1f6fc0 0%,#123a66 40%,#c9ccd0 75%,#eef0f2 100%)}
.gallery-item.mid{width:200px;height:345px;background:linear-gradient(180deg,#2a2d31 0%,#0f1114 30%,#1d4f86 50%,#0f1114 70%,#2a2d31 100%)}
.sub-kicker{top:508px;font-size:25px;font-weight:500;color:var(--white)}
.sub-title{top:546px;font-size:35px;font-weight:800;color:var(--white);letter-spacing:.5px}
.email-bar{left:240px;top:608px;width:720px;height:44px;border-radius:22px;background:var(--white);display:flex;align-items:center}
.email-bar .icon{width:36px;height:28px;border-right:1px solid var(--line);display:flex;align-items:center;justify-content:center;margin-left:10px}
.email-bar input{flex:1;border:0;outline:0;font-family:inherit;font-size:11px;color:var(--text);padding-left:14px;background:transparent}
.email-bar input::placeholder{color:var(--text)}
.email-bar button{width:124px;height:36px;margin-right:4px;border:0;border-radius:18px;background:var(--blue-bright);color:var(--white);font-family:inherit;font-size:12px;font-weight:600}

/* footer */
.site-footer{top:3648px;height:417px}
.footer-brand{left:95px;top:72px;width:180px;text-align:center}
.footer-brand .mark{width:36px;height:36px;background:var(--blue);margin:0 auto 8px}
.footer-brand .name{font-size:32px;font-weight:700;color:var(--blue);letter-spacing:2px}
.footer-about{left:95px;top:212px;width:250px;font-size:12px;line-height:21px;color:var(--text)}
.footer-col{top:78px}
.footer-col h5{font-size:22px;font-weight:400;letter-spacing:.5px;margin-bottom:16px}
.footer-col li{list-style:none;font-size:12px;color:var(--muted);height:30px}
.social li{display:flex;align-items:center;gap:10px;height:38px}
.social .dot{width:26px;height:26px;border-radius:50%;border:1px solid var(--line)}
.copyright{font-size:11px;color:var(--text)}
.copyright b{color:var(--blue);font-weight:500}
</style>
</head>
<body>

<header class="site-nav">
  <div class="abs brand"><span class="brand-mark"></span>VORTEK</div>
  <a class="abs nav-link active" style="left:723px">HOME</a>
  <a class="abs nav-link" style="left:804px">FEATURES</a>
  <a class="abs nav-link" style="left:908px">TECH &amp; SPECS</a>
  <a class="abs nav-link" style="left:1034px">CONTACT US</a>
</header>

<section class="hero">
  <div class="abs hero-visual" role="img" aria-label="Smart watch splashing through water"></div>
  <h1 class="abs hero-title">VORTEK</h1>
  <h2 class="abs hero-sub">The Ultimate Smart Watch</h2>
  <p class="abs hero-copy">VORTEK Studio is a mobile and multiexperience application design company intended for the industry and particularly the watch industry.</p>
  <a class="abs btn-outline">GET STARTED</a>
</section>

<section class="features">
  <h2 class="abs center section-title" style="top:65px">WATCH SMARTER</h2>
  <p class="abs center section-sub" style="top:114px">There are many variations of passages of Lorem Ipsum available</p>
  <div class="abs feature" style="left:121px;top:190px">
    <div class="watch-art" role="img" aria-label="Watch showing start swimming screen"></div>
    <h3>Intencity Coach</h3>
    <p>Sed ut perspiciatis unde omnis iste natus error sit voluptatem</p>
  </div>
  <div class="abs feature" style="left:460px;top:190px">
    <div class="watch-art" role="img" aria-label="Watch showing pace and heart rate"></div>
    <h3>Pace Keeper</h3>
    <p>Sed ut perspiciatis unde omnis iste natus error sit voluptatem</p>
  </div>
  <div class="abs feature" style="left:797px;top:190px">
    <div class="watch-art" role="img" aria-label="Watch showing interval training screen"></div>
    <h3>Training Guide</h3>
    <p>Sed ut perspiciatis unde omnis iste natus error sit voluptatem</p>
  </div>
</section>

<section class="app">
  <div class="abs app-visual" role="img" aria-label="Fitness app screens on phones showing activity and progression charts"></div>
  <h2 class="abs section-title" style="left:682px;top:62px">MORE THAN A WATCH</h2>
  <p class="abs section-sub" style="left:682px;top:112px;width:400px">There are many variations of passages of Lorem Ipsum available</p>
  <div class="abs check-list">
    <div class="check-item"><div class="ring"><span></span></div><div><h4>The standard Lorem Ipsum passage</h4><p>Sed ut perspiciatis unde omnis iste natus error sit voluptatem accusantium</p></div></div>
    <div class="check-item"><div class="ring"><span></span></div><div><h4>The standard Lorem Ipsum passage</h4><p>Sed ut perspiciatis unde omnis iste natus error sit voluptatem accusantium</p></div></div>
    <div class="check-item"><div class="ring"><span></span></div><div><h4>The standard Lorem Ipsum passage</h4><p>Sed ut perspiciatis unde omnis iste natus error sit voluptatem accusantium</p></div></div>
  </div>
</section>

<section class="tech">
  <div class="abs tech-visual" role="img" aria-label="Holographic smart watch with glowing blue interface"></div>
  <h2 class="abs section-title" style="left:95px;top:52px">MORE THAN A WATCH</h2>
  <p class="abs section-sub" style="left:95px;top:102px;width:400px">There are many variations of passages of Lorem Ipsum available</p>
  <div class="abs tech-list">
    <div class="tech-item"><div class="ring"><span></span></div>Usable on Watches</div>
    <div class="tech-item"><div class="ring"><span></span></div>Holographic Screens</div>
    <div class="tech-item"><div class="ring"><span></span></div>Giant Touch Screens</div>
    <div class="tech-item"><div class="ring"><span></span></div>Virtual Reality</div>
    <div class="tech-item"><div class="ring"><span></span></div>Remotely with a Gripsense</div>
  </div>
</section>

<section class="partners">
  <h2 class="abs section-title" style="left:95px;top:64px;line-height:47px">THE STANDARD<br>LOREM IPSUM PASSAGE</h2>
  <p class="abs">Sed ut perspiciatis unde omnis iste natus error sit voluptatem accusantium doloremque laudantium, totam rem aperiam, eaque ipsa quae ab illo inventore veritatis</p>
  <div class="abs badge-grid" aria-label="Partners">
    <div class="badge"><span></span></div><div class="badge"><span></span></div><div class="badge"><span></span></div><div class="badge"><span></span></div>
    <div class="badge"><span></span></div><div class="badge"><span></span></div><div class="badge"><span></span></div><div class="badge"><span></span></div>
  </div>
</section>

<section class="health">
  <div class="abs health-visual" role="img" aria-label="Hands holding a smart watch and a phone showing heart rate"></div>
  <h2 class="abs section-title" style="left:682px;top:106px;line-height:47px">THE STANDARD<br>LOREM IPSUM PASSAGE</h2>
  <p class="abs">Sed ut perspiciatis unde omnis iste natus error sit voluptatem accusantium doloremque laudantium, totam rem aperiam, eaque ipsa quae ab illo inventore veritatis</p>
  <a class="abs btn-solid">READ MORE</a>
</section>

<section class="subscribe">
  <div class="abs gallery" aria-label="Watch gallery">
    <div class="gallery-item side dark" role="img" aria-label="Black smart watch with curved blue display"></div>
    <div class="gallery-item mid" role="img" aria-label="Square black smart watch with analog dial face"></div>
    <div class="gallery-item side silver" role="img" aria-label="Silver smart watch with curved blue display"></div>
  </div>
  <p class="abs center sub-kicker">DON'T MISS THE DAY</p>
  <h2 class="abs center sub-title">WHEN VORTEK IS AVAILABLE!</h2>
  <form class="abs email-bar">
    <div class="icon"><svg width="12" height="9" viewBox="0 0 12 9"><rect x="0.5" y="0.5" width="11" height="8" fill="#2b2f36"/><path d="M0.5 0.5 6 5 11.5 0.5" stroke="#fff" fill="none"/></svg></div>
    <input type="email" placeholder="Enter Your Email" aria-label="Email address">
    <button type="submit">Subscribe</button>
  </form>
</section>

<footer class="site-footer">
  <div class="abs footer-brand"><div class="mark"></div><div class="name">VORTEK</div></div>
  <p class="abs footer-about">But I must explain to you how all this mistaken idea of denouncing pleasure and praising pain was born</p>
  <div class="abs footer-col" style="left:407px"><h5>FEATURES</h5><ul><li>Nam libero</li><li>Itaque earum</li><li>Voluptatibus Maiores</li><li>Nam libero</li><li>Itaque earum</li><li>Voluptatibus Maiores</li></ul></div>
  <div class="abs footer-col" style="left:627px"><h5>DO YOU USE</h5><ul><li>Orchard Watch</li><li>Fitpulse</li><li>Garnet Watch</li><li>Lorem Ipsum</li><li>Lorem Dolar</li><li>Ipsum Dolar</li></ul></div>
  <div class="abs footer-col" style="left:829px"><h5>COMPANY</h5><ul><li>Home</li><li>About Us</li><li>Features</li><li>Media &amp; Press</li><li>Terms &amp; Condition</li><li>Contact Us</li></ul></div>
  <div class="abs footer-col social" style="left:1007px"><h5>SOCIAL</h5><ul>
    <li><span class="dot"></span>Facenet</li><li><span class="dot"></span>Chirper</li><li><span class="dot"></span>Linkpro</li><li><span class="dot"></span>Instasnap</li><li><span class="dot"></span>Chatwave</li></ul></div>
  <p class="abs center copyright" style="top:336px">COPYRIGHT © 2020 <b>VORTEK STUDIO</b>. ALL RIGHTS RESERVED.</p>
</footer>

</body>
</html>
```